Private Practice Dietitian's Business Card

A 2-sided business card for a dietitian (medical nutritionist) in private practice within a natural therapies allied health clinic. The business card needs to imply warmth and professionalism.
Target Market(s)
Doctors who may refer patients to a dietitian and patients themselves who may request dietetic assessment, education and counselling.
Industry/Entity Type
Business
Requirements
Must have
- The business card must be an intense blue on the front at the bottom, gradually lightening towards the top of the card. Please see:
http://pinboardly.example/rupert_halvane/card-ideas/
for an example from "The quiet of the riverbank" book. I'd like an apple tree on the left with a pale silver/grey trunk (like the silver in the book cover)and branches that bends over to the right above the writing. Apples to be a turquoise/aqua colour similar to that in "The quiet of the riverbank" book cover. Front cover writing to read:
foodsteps
0462 883 917
foodsteps@kelvanet.example
'foodsteps' is one word but I would like the 'my' in turquoise/aqua to match the apples and the 'dietitian' and the phone number and email address in the pale silver/grey to match the tree trunk.
I'd like the foodsteps in larger font than the phone number and email address but for all 3 lines of text on the front of the business card to be stretched so they have the same left and right margin. (I hope this makes sense!)
I would like the back of the card to be white and the top section of text to be in the same turquoise/aqua from the apples on the front of the card and to read:
MAREE TOLVIN
Accredited Practising Dietitian (APD)
Bachelor of Health Science (Nutrition & Dietetics) - Honours
Master of Nutrition & Dietetics
This text should be stretched/compacted so that it all has the same left and right margin.
After this text there should be a blank line for spacing before the next section of text, which is to be in the silver/grey of the tree trunk. It should read:
Weight management
Diabetes
Impaired fasting glycaemia
Impaired glucose tolerance
Gestational diabetes
Wellness & general nutrition
Cardiovascular disease
high blood pressure
High cholesterol
High triglycerides
Fatty liver
Constipation
Diverticular disease
Coeliac disease
Irritable bowel syndrome
Gastroesophageal reflux
Lactose intolerance
Gout
Polycystic ovarian syndrome
Fertility
Pregnancy
Breastfeeding
Osteoporosis
Iron deficiency
Vegetarian eating
This set of text can run across the page from left to right and each medical condition could be separated from the next in some way to help with ease of reading. For example perhaps a space, dot and another space could separate the medical conditions. This set of text should be stretched so that the left and right margins of each line is the same. Thank you!
Nice to have
- An easy-to read but 'elegant' font would be nice - but I have no idea which one! Nothing too ornate, but not dull standard Times New Roman/Arial/Comic Sans either!
Should not have
- Times new roman/comic sans/arial fonts

```html
<!DOCTYPE html>
<html lang="en">
<head>
<meta charset="utf-8">
<title>foodsteps – business card</title>
<link rel="stylesheet" href="https://fonts.googleapis.com/css2?family=Ubuntu:wght@400;500&display=swap">
<style>
  :root {
    --stage: #3a3a3a;
    --blue-deep: #0a1a8c;
    --blue-mid: #1a2fc4;
    --blue-light: #2f4bd6;
    --aqua: #62d3e6;
    --silver: #c9ccd6;
    --white: #f2f4fa;
    --band: #050508;
    --ornament-a: #9aa0ac;
    --ornament-b: #4fb8d4;
  }
  * { box-sizing: border-box; margin: 0; padding: 0; }
  html, body {
    width: 1200px; height: 800px; overflow: hidden;
    background: var(--stage);
    font-family: "Ubuntu", "Trebuchet MS", sans-serif;
  }
  .sheet {
    width: 1200px; height: 800px;
    display: flex; align-items: center; justify-content: center; gap: 40px;
  }
  .card {
    position: relative;
    width: 540px; height: 330px;
    overflow: hidden;
    background: radial-gradient(ellipse at 30% 20%, var(--blue-light) 0%, var(--blue-mid) 40%, var(--blue-deep) 100%);
  }

  /* back */
  .card-back .credentials { position: absolute; left: 34px; top: 44px; }
  .card-back .name {
    color: var(--aqua); font-size: 24px; font-weight: 400; letter-spacing: 0.5px;
    margin-bottom: 6px;
  }
  .card-back .qual { color: var(--silver); font-size: 13.5px; line-height: 1.45; }
  .services {
    position: absolute; left: 18px; right: 18px; bottom: 20px;
    background: var(--band); border-radius: 8px;
    padding: 12px 14px;
    color: var(--silver); font-size: 12.5px; line-height: 1.55;
    text-align: justify; text-align-last: center;
  }

  /* front */
  .ornament {
    position: absolute; left: 0; top: 30px; width: 230px; height: 270px;
    border-radius: 0 60% 50% 0;
    background: radial-gradient(circle at 72% 30%, var(--ornament-b) 0%, rgba(79,184,212,0.4) 18%, rgba(154,160,172,0.35) 40%, rgba(154,160,172,0) 72%);
  }
  .contact {
    position: absolute; left: 230px; top: 170px; width: 270px;
    text-align: right;
  }
  .brand { color: var(--aqua); font-size: 50px; font-weight: 500; line-height: 1; letter-spacing: 0.5px; }
  .contact .line { color: var(--white); font-size: 17px; line-height: 1.3; }
  .contact .phone { margin-top: 8px; }
</style>
</head>
<body>
<main class="sheet">
  <section class="card card-back" aria-label="Card back">
    <div class="credentials">
      <h1 class="name">MAREE TOLVIN</h1>
      <p class="qual">Accredited Practising Dietitian (APD)</p>
      <p class="qual">Bachelor of Health Science (Nutrition &amp; Dietetics) - Honours</p>
      <p class="qual">Master of Nutrition &amp; Dietetics</p>
    </div>
    <p class="services">Weight management · Diabetes · Impaired fasting glycaemia · Impaired glucose tolerance · Gestational diabetes · Wellness &amp; general nutrition · Cardiovascular disease · High blood pressure · High cholesterol · High triglycerides · Fatty liver · Constipation · Diverticular disease · Coeliac disease · Irritable bowel syndrome · Gastroesophageal reflux · Lactose intolerance · Gout · Polycystic ovarian syndrome · Fertility · Pregnancy · Breastfeeding · Osteoporosis · Iron deficiency · Vegetarian eating</p>
  </section>

  <section class="card card-front" aria-label="Card front">
    <div class="ornament" role="img" aria-label="Silver swirling apple tree branch bending right, holding a glossy turquoise apple"></div>
    <div class="contact">
      <p class="brand">foodsteps</p>
      <p class="line phone">0462 883 917</p>
      <p class="line email">foodsteps@kelvanet.example</p>
    </div>
  </section>
</main>
</body>
</html>
```